Wattlebrook Legal: Sole Practitioner Law Firm seeking corporate branding drawing on unique bush setting

I need a logo, stationary and business card design for my law firm. I will be practising as a sole practitioner specialising in corporate, commercial, finance, migration and agriculture law. Having left my corporate job in the city and relocated our family to our farm in regional Western Australia, I would like the corporate design for my company to be crisp, stylish, concise and uncomplicated. The law firm is called "Wattlebrook Legal" because we have a colony of the endangered Carnaby Black Cockatoos living in the bush behind our homestead (which is also my office). I will travel to clients rather than have them visit me. I would like to see a stylised image of the bird with some Australian native bush included in the design, either as a background image on the back of the card. A separate brief has been created for the logo and stationary though I hope all 3 pieces of work will "marry". The final design should communicate clarity of vision, efficiency, compassion and solution/ outcome focused. I prefer to have the business cards printed on card with a bit of texture and substance. I will try not to use laminated card as I consider it feels "plastic and commoditised" which is inconsistent with the image and feel of the business I intend creating. Please see attached brief for further details of the design brief.

Target Market(s)

Agriculture and Horticulture companies, Farmers, Family offices and estates, banks, insurance companies, individuals wishing to migrate to Australia

Industry/Entity Type

Legal

Contact Information for Business Card

Harriet Lyle-Pemberton
LLB (Hons), BSc., MEc.
Legal Practitioner and Director

WATTLEBROOK LEGAL PTY LTD
PO Box 726, Emuvale WA 6391
Ph: 0452 781906
Email: harrietlp@ferncastmail.com

Solicitor admitted to practice in the Upper Bench of Kestrel Shore, England and Wales, NSW, and Registered Practitioner of the Chief Bench of Marrowdale

Logo Text

WATTLEBROOK LEGAL: Client Focused Commercial Legal Solutions

Font styles to use
Other font styles liked:
• Verlag

Colors
ec1f27
fbee3d
9bcb3c
ffffff
1b1b1b
c4c4c4

Requirements
Must have
• A look and feel of quality, conservatism, adventure
Nice to have
• A stylised image of a Carnaby Cockatoo and Australian flora as a background image or design on the back of the card.
Should not have
• Clutter, cartoons

```html
<!DOCTYPE html>
<html lang="en">
<head>
<meta charset="utf-8">
<title>Wattlebrook Legal — Business Card</title>
<link rel="stylesheet" href="https://fonts.googleapis.com/css2?family=Cinzel:wght@400&family=Libre+Baskerville:wght@700&family=Open+Sans:wght@400&family=Tinos&display=swap">
<style>
  :root {
    --backdrop: #ececec;
    --card-white: #fbfbfa;
    --wattle-orange: #eea21a;
    --ink-grey: #4a4a4a;
    --paper: #ffffff;
  }
  * { box-sizing: border-box; margin: 0; padding: 0; }
  html, body {
    width: 1200px; height: 900px; overflow: hidden;
    background: var(--backdrop);
  }
  .card-set {
    position: absolute; inset: 0;
    display: flex; align-items: center; justify-content: center; gap: 60px;
  }
  .card {
    position: relative;
    width: 520px; height: 318px;
    box-shadow: 0 2px 8px rgba(0,0,0,0.12);
  }
  /* Front */
  .card-front { background: var(--card-white); }
  .holder {
    position: absolute; left: 34px; top: 30px;
  }
  .holder-name {
    font-family: "Libre Baskerville", Georgia, serif;
    font-weight: 700; font-variant: small-caps;
    font-size: 19px; letter-spacing: 0.5px;
    color: var(--wattle-orange);
  }
  .holder-detail {
    font-family: "Open Sans", Arial, sans-serif;
    font-size: 12px; line-height: 17px; color: var(--ink-grey);
    margin-top: 4px;
  }
  .contact-list {
    position: absolute; left: 34px; top: 122px;
    list-style: none;
    font-family: "Open Sans", Arial, sans-serif;
    font-size: 12px; line-height: 20px; color: var(--ink-grey);
  }
  .contact-list li { display: flex; align-items: center; gap: 8px; }
  .contact-list svg { width: 10px; height: 10px; fill: var(--wattle-orange); }
  .wordmark {
    font-family: "Cinzel", "Times New Roman", serif;
    font-weight: 400; white-space: nowrap;
    display: flex; align-items: center; gap: 10px;
  }
  .wordmark-dot {
    width: 12px; height: 12px; border-radius: 50%;
  }
  .front-wordmark {
    position: absolute; right: 34px; top: 180px;
    font-size: 30px; line-height: 40px; color: var(--wattle-orange);
  }
  .front-wordmark .wordmark-dot { background: var(--wattle-orange); }
  .company-address {
    position: absolute; right: 34px; bottom: 28px;
    text-align: right;
    font-family: "Open Sans", Arial, sans-serif;
    font-size: 12px; line-height: 17px; color: var(--ink-grey);
  }
  /* Back */
  .card-back { background: var(--wattle-orange); }
  .back-wordmark {
    position: absolute; left: 0; right: 0; top: 92px;
    justify-content: center;
    font-size: 32px; line-height: 42px; color: var(--paper);
  }
  .back-wordmark .wordmark-dot { background: var(--paper); }
  .admission {
    position: absolute; left: 90px; right: 90px; top: 160px;
    text-align: center;
    font-family: "Tinos", "Times New Roman", serif;
    font-size: 13px; line-height: 18px; color: var(--paper);
  }
</style>
</head>
<body>
  <main class="card-set">
    <section class="card card-front" aria-label="Card front">
      <div class="holder">
        <p class="holder-name">Harriet Lyle-Pemberton</p>
        <p class="holder-detail">LLB (Hons), BSc., MEc.<br>Legal Practitioner and Director</p>
      </div>
      <ul class="contact-list">
        <li>
          <svg viewBox="0 0 10 10" aria-hidden="true"><path d="M2 0.5 L3.6 0.5 L4.3 2.8 L3.2 3.6 Q4.2 5.8 6.4 6.8 L7.2 5.7 L9.5 6.4 L9.5 8 Q9.5 9.5 8 9.5 Q0.5 9 0.5 2 Q0.5 0.5 2 0.5 Z"/></svg>
          0452 781906
        </li>
        <li>
          <svg viewBox="0 0 10 10" aria-hidden="true"><rect x="0" y="1.5" width="10" height="7" rx="1"/></svg>
          harrietlp@ferncastmail.com
        </li>
      </ul>
      <div class="wordmark front-wordmark">
        <span class="wordmark-dot" aria-hidden="true"></span>
        <span>Wattlebrook Legal</span>
      </div>
      <p class="company-address">WATTLEBROOK LEGAL PTY LTD<br>PO Box 726, Emuvale WA 6391</p>
    </section>

    <section class="card card-back" aria-label="Card back">
      <div class="wordmark back-wordmark">
        <span class="wordmark-dot" aria-hidden="true"></span>
        <span>Wattlebrook Legal</span>
      </div>
      <p class="admission">Solicitor admitted to practice in the Upper Bench of Kestrel Shore, England and Wales, NSW, and Registered Practitioner of the Chief Bench of Marrowdale</p>
    </section>
  </main>
</body>
</html>
```